Website design for recruitment solutions

We connect top talents to fast growing employers in Asia. We need to revamp our existing website (currently outdated) and also add more pages to make it more informative for talents and employers.
We need final design output to be for both desktop and mobile devices. The final design output must come with all specifications so it's easier for our dev team to implement. We have a detailed mockup but we expect the design to be significantly changed by the final output. We want the pages to look aesthetic, modern and professional.
Number of Pages Required
5+ page
Requirements
Must have
- - To have Pages design for desktop+mobile. Need to take into account intermediate resolutions like 1365px\1023px\767px\479px, especially if mobile/desktop design differs considerably. Design should be repeatable (between pages), suitable for block-layout.
Nice to have
- In terms of receiving files, we usually work with designers who can deliver files in Figma or Sketch with export to Figma. If in PSD format - please export to Zeplin or Avocode, otherwise will be difficult to open

```html
<!DOCTYPE html>
<html lang="en">
<head>
<meta charset="utf-8">
<title>Talentra – Recruitment Solutions</title>
<link href="https://fonts.googleapis.com/css2?family=Roboto:wght@300;400;500;700&display=swap" rel="stylesheet">
<style>
:root{
  --hero-blue:#4d73a6;
  --brand-blue:#53709b;
  --title-blue:#4e6d99;
  --accent-red:#f50000;
  --accent-yellow:#f7c21c;
  --nav-dark:#222222;
  --text-grey:#6b6b6b;
  --band-grey:#f3f3f3;
  --white:#ffffff;
  --art-light:#b6dcf7;
  --art-mid:#8fc3ee;
}
*{margin:0;padding:0;box-sizing:border-box}
html,body{width:1200px;height:2789px;overflow:hidden}
body{position:relative;background:var(--white);font-family:"Roboto",sans-serif;color:var(--text-grey)}
.abs{position:absolute}

/* hero */
.hero{left:0;top:0;width:1200px;height:730px;background:var(--hero-blue)}
.hero-art{left:0;top:119px;width:585px;height:606px;background:radial-gradient(ellipse at 45% 40%,#e9eef4 0%,#aebfd3 45%,#3c4350 80%,#4d73a6 100%);border-radius:8px}
.hero-wave{left:0;top:440px}
.logo{left:129px;top:22px;width:117px;height:43px;border:1.5px solid rgba(255,255,255,.85);color:var(--white);font-size:22px;font-weight:400;display:flex;align-items:center;justify-content:center;letter-spacing:.5px}
.nav{left:358px;top:35px;display:flex;gap:21px;font-size:14.5px;font-weight:500;color:var(--white);letter-spacing:.3px}
.nav .is-active{color:var(--accent-yellow)}
.btn-register,.btn-login{top:27px;height:35px;width:99px;color:var(--white);font-size:14.5px;font-weight:500;display:flex;align-items:center;justify-content:center}
.btn-register{left:880px;background:var(--accent-red)}
.btn-login{left:985px;background:var(--nav-dark)}
.headline{left:615px;top:150px;color:var(--white);font-size:41px;font-weight:300;letter-spacing:8.5px;line-height:70.5px}
.headline .lead{color:var(--accent-yellow);font-weight:700;font-size:56px;letter-spacing:4px}
.btn-start{left:614px;top:476px;width:220px;height:64px;background:var(--accent-red);color:var(--white);font-size:23px;font-weight:500;letter-spacing:.8px;display:flex;align-items:center;justify-content:center}

/* features */
.feature-art{width:417px;height:276px;background:linear-gradient(160deg,var(--art-light),var(--art-mid))}
.feature-title{font-size:28px;font-weight:700;color:var(--title-blue);letter-spacing:.6px}
.feature-rule{height:2px;width:111px;background:var(--title-blue)}
.feature-text{font-size:13px;font-weight:400;line-height:21px;color:var(--text-grey);width:370px}
.band{left:0}

/* testimonials */
.section-title{left:0;width:1200px;text-align:center;font-size:28px;font-weight:700;color:var(--title-blue)}
.section-sub{left:0;width:1200px;text-align:center;font-size:13px;color:var(--text-grey)}
.quote-card{background:var(--white);padding:38px 18px 0 24px;font-size:9px;line-height:20px;color:#555}
.quote-card.is-featured{background:var(--brand-blue);color:var(--white);font-size:11px;line-height:23px;padding:40px 16px 0 35px}
.quote-mark{position:absolute;font-size:34px;font-weight:700;font-style:italic;color:#8a8a8a;line-height:1}
.is-featured .quote-mark{color:var(--white)}
.card-tail{width:0;height:0;border-style:solid}
.avatar{border-radius:50%;background:linear-gradient(180deg,#c8dced 0%,#8aa7c2 55%,#3c4a5c 100%)}
.person-name{font-size:14px;color:#333}
.person-role{font-size:11px;color:var(--title-blue)}

/* footer */
.footer{left:0;top:2404px;width:1200px;height:385px;background:var(--brand-blue);color:var(--white)}
.footer-heading{font-size:21px;font-weight:700;letter-spacing:.8px}
.footer-text{font-size:12.5px;line-height:21px}
.footer-link{font-size:12.5px;line-height:30px}
.footer-divider{width:1px;background:rgba(255,255,255,.7)}
.footer-rule{left:109px;top:231px;width:975px;height:1px;background:rgba(255,255,255,.7)}
.copyright{font-size:8px}
.address{font-size:12.5px;line-height:23px}
</style>
</head>
<body>

<!-- Hero -->
<header class="abs hero">
  <div class="abs hero-art" role="img" aria-label="Illustration of a desktop computer showing candidate profile cards and a woman working at a desk, with keyboard and mouse"></div>
</header>
<svg class="abs hero-wave" width="1200" height="320" viewBox="0 440 1200 320" aria-hidden="true">
  <path d="M0 693 C120 700 250 745 361 723 C470 700 520 600 603 571 C700 540 820 660 937 666 C1040 672 1080 520 1191 507 L1200 506 L1200 760 L0 760 Z" fill="#ffffff"/>
  <g fill="#ffffff" stroke="#4d73a6" stroke-width="3">
    <circle cx="152" cy="667" r="6"/>
    <circle cx="361" cy="723" r="6"/>
    <circle cx="603" cy="571" r="6"/>
    <circle cx="937" cy="666" r="6"/>
    <circle cx="1191" cy="507" r="6"/>
  </g>
</svg>

<div class="abs logo">TALENTRA</div>
<nav class="abs nav">
  <span class="is-active">HOME</span>
  <span>HOW WE WORK</span>
  <span>BROWSE JOBS</span>
  <span>EMPLOYERS</span>
  <span>ABOUT US</span>
</nav>
<div class="abs btn-register">Register</div>
<div class="abs btn-login">Log In</div>

<h1 class="abs headline"><span class="lead">W</span>e connect top<br>talents into fast<br>growing employers<br>in Asia.</h1>
<div class="abs btn-start">Get Started</div>

<!-- Smart Connections -->
<div class="abs feature-art" style="left:170px;top:771px" role="img" aria-label="Isometric illustration of connected devices, servers and cloud storage"></div>
<h2 class="abs feature-title" style="left:667px;top:767px">Smart Connections</h2>
<div class="abs feature-rule" style="left:669px;top:813px"></div>
<p class="abs feature-text" style="left:670px;top:840px">It's the quality of the connection that matters. Our role matching algorithms and talent managers work around the clock to find opportunities suitable to your unique profile.</p>

<!-- Critical Insights band -->
<svg class="abs band" style="top:1085px" width="1200" height="464" viewBox="0 0 1200 464" aria-hidden="true">
  <path d="M0 103 C250 20 450 5 620 3 C850 0 1050 40 1200 115 L1200 462 L0 462 Z" fill="#f3f3f3"/>
</svg>
<h2 class="abs feature-title" style="left:165px;top:1210px">Critical Insights</h2>
<div class="abs feature-rule" style="left:170px;top:1258px"></div>
<p class="abs feature-text" style="left:169px;top:1284px">Our close interactions with candidates and employers have helped us create a comprehensive database of companies, talents and skills. With TALENTRA, you will gain full access to timely intel to help you make the right career decision.</p>
<div class="abs feature-art" style="left:610px;top:1203px" role="img" aria-label="Illustration of a team working together at desks with screens and chat bubbles"></div>

<!-- People First -->
<div class="abs feature-art" style="left:170px;top:1602px" role="img" aria-label="Illustration of people meeting and reviewing candidate profiles"></div>
<h2 class="abs feature-title" style="left:671px;top:1597px">People First</h2>
<div class="abs feature-rule" style="left:671px;top:1644px"></div>
<p class="abs feature-text" style="left:670px;top:1671px">We take the time to really understand you holistically as a person to maximize your potential. As your career counselor, we provide maximum transparency and feedback throughout the process.</p>

<!-- Testimonials band -->
<svg class="abs band" style="top:1945px" width="1200" height="460" viewBox="0 0 1200 460" aria-hidden="true">
  <path d="M0 96 C230 30 420 3 610 2 C830 0 1040 40 1200 140 L1200 460 L0 460 Z" fill="#f3f3f3"/>
</svg>
<h2 class="abs section-title" style="top:2004px">Testimonial</h2>
<p class="abs section-sub" style="top:2044px">Lorem Ipsum is simply dummy text of the printing and typesetting industry.</p>

<div class="abs quote-card" style="left:168px;top:2113px;width:250px;height:145px">
  <span class="quote-mark" style="left:6px;top:20px">&ldquo;</span>
  Lorem ipsum dolor sit amet, consectetur adipiscing elit, sed do eiusmod tempor incididunt ut labore et dolore magna aliqua. Quis ipsum suspendisse ultrices gravida.
  <span class="quote-mark" style="left:160px;top:98px">&rdquo;</span>
</div>
<div class="abs card-tail" style="left:213px;top:2258px;border-width:0 28px 12px 0;border-color:transparent #ffffff transparent transparent"></div>
<div class="abs avatar" style="left:165px;top:2272px;width:49px;height:49px" role="img" aria-label="Portrait photo of the client"></div>
<div class="abs person-name" style="left:227px;top:2276px">Arin Vale</div>
<div class="abs person-role" style="left:229px;top:2294px">Doctor</div>

<div class="abs quote-card is-featured" style="left:447px;top:2101px;width:307px;height:173px">
  <span class="quote-mark" style="left:10px;top:20px">&ldquo;</span>
  Lorem Ipsum is simply dummy text of the printing and typesetting industry. Lorem Ipsum has been the industry's standard dummy text ever since the 1500s
  <span class="quote-mark" style="left:198px;top:118px">&rdquo;</span>
</div>
<div class="abs card-tail" style="left:500px;top:2274px;border-width:0 28px 14px 0;border-color:transparent #53709b transparent transparent"></div>
<div class="abs avatar" style="left:443px;top:2288px;width:59px;height:59px" role="img" aria-label="Portrait photo of the client"></div>
<div class="abs person-name" style="left:516px;top:2296px;font-size:16px">Arin Vale</div>
<div class="abs person-role" style="left:519px;top:2317px;font-size:12px">Doctor</div>

<div class="abs quote-card" style="left:781px;top:2113px;width:249px;height:145px">
  <span class="quote-mark" style="left:4px;top:20px">&ldquo;</span>
  Lorem ipsum dolor sit amet, consectetur adipiscing elit, sed do eiusmod tempor incididunt ut labore et dolore magna aliqua. Quis ipsum suspendisse ultrices gravida.
  <span class="quote-mark" style="left:160px;top:98px">&rdquo;</span>
</div>
<div class="abs card-tail" style="left:826px;top:2258px;border-width:0 28px 12px 0;border-color:transparent #ffffff transparent transparent"></div>
<div class="abs avatar" style="left:777px;top:2272px;width:49px;height:49px" role="img" aria-label="Portrait photo of the client"></div>
<div class="abs person-name" style="left:839px;top:2276px">Arin Vale</div>
<div class="abs person-role" style="left:841px;top:2294px">Doctor</div>

<!-- Footer -->
<footer class="abs footer">
  <h3 class="abs footer-heading" style="left:114px;top:38px">ABOUT US</h3>
  <p class="abs footer-text" style="left:114px;top:90px;width:240px">Lorem Ipsum is simply dummy text of the printing and typesetting industry. Lorem Ipsum has been the industry's standard dummy text ever since the 1500s, when an unknown printer took a galley of type and</p>

  <div class="abs footer-divider" style="left:419px;top:31px;height:168px"></div>
  <h3 class="abs footer-heading" style="left:469px;top:38px">TALENTS</h3>
  <div class="abs footer-link" style="left:470px;top:82px">How it works<br>Browse jobs</div>

  <div class="abs footer-divider" style="left:612px;top:31px;height:168px"></div>
  <h3 class="abs footer-heading" style="left:668px;top:38px">EMPLOYERS</h3>
  <div class="abs footer-link" style="left:668px;top:82px">How it works</div>

  <div class="abs footer-divider" style="left:863px;top:31px;height:168px"></div>
  <h3 class="abs footer-heading" style="left:945px;top:38px">ABOUT US</h3>
  <div class="abs footer-link" style="left:945px;top:82px">About&nbsp; TALENTRA<br>Working at&nbsp; TALENTRA</div>

  <div class="abs footer-rule"></div>

  <div class="abs copyright" style="left:113px;top:278px">@ TALENTRA 2012-2020&nbsp; All rights reserved.</div>

  <svg class="abs" style="left:421px;top:260px" width="22" height="32" viewBox="0 0 22 32" aria-hidden="true">
    <path d="M11 0C4.9 0 0 4.9 0 11c0 8 11 21 11 21s11-13 11-21C22 4.9 17.1 0 11 0z" fill="#ffffff"/>
    <circle cx="11" cy="11" r="4.5" fill="#53709b"/>
  </svg>
  <p class="abs address" style="left:470px;top:258px;width:240px">Harbourline Staffing Limited (EA License No. 40217) Room 12, Level 5, Tower 2, 88 Seaview Road, Kowloon Bay, Hong Kong</p>

  <svg class="abs" style="left:754px;top:260px" width="22" height="32" viewBox="0 0 22 32" aria-hidden="true">
    <path d="M11 0C4.9 0 0 4.9 0 11c0 8 11 21 11 21s11-13 11-21C22 4.9 17.1 0 11 0z" fill="#ffffff"/>
    <circle cx="11" cy="11" r="4.5" fill="#53709b"/>
  </svg>
  <p class="abs address" style="left:802px;top:258px;width:230px">Talentra Pte. Ltd. (License No. 19C4402) 42 Marina Crest Rd, #11-02 Bayfront House, Singapore 049211</p>
</footer>

</body>
</html>
```